Vorlan cards

I am in the auto motive, transportation business I would like a business card that is Something cool, modern edgy, having to do with car culture. I offer towing service for high and exotic cars. I also provide towing for collisions and car accidents. I offer open and enclosed transport nationwide.

Target Market(s)

Car culture people high end auto collectors

Industry/Entity Type

Towing car carrier

Contact Information for Business Card

My company colors black yellow and silver

Font styles to use
Serif

```html
<!DOCTYPE html>
<html lang="en">
<head>
<meta charset="utf-8">
<title>Vorlan Transportation – Business Cards</title>
<link rel="stylesheet" href="https://fonts.googleapis.com/css2?family=Arimo:wght@400;700&display=swap">
<style>
  :root {
    --bg: #e4e4e4;
    --card-white: #ffffff;
    --card-dark: #2f2f2f;
    --art-tone: #3b3b3b;
    --art-warm: #403d30;
    --yellow: #f2cf2e;
    --ink: #111111;
    --grey-text: #7a7a7a;
    --divider: #9a9a9a;
    --white: #ffffff;
  }
  * { box-sizing: border-box; margin: 0; padding: 0; }
  html, body { width: 1200px; height: 802px; overflow: hidden; }
  body {
    background: var(--bg);
    font-family: "Arimo", Arial, sans-serif;
    position: relative;
  }
  .card {
    position: absolute;
    top: 258px;
    width: 510px;
    height: 292px;
    border-bottom: 4px solid var(--yellow);
    border-right: 3px solid var(--yellow);
    overflow: hidden;
  }
  .card--front { left: 60px; background: var(--card-white); }
  .card--back { left: 630px; background: var(--card-dark); }

  /* front */
  .brand-mark {
    position: absolute;
    left: 150px; top: 42px;
    display: flex; align-items: center; gap: 8px;
  }
  .brand-dot {
    width: 16px; height: 16px; border-radius: 50%;
    background: var(--yellow);
  }
  .brand-name {
    font-weight: 700; font-size: 30px; letter-spacing: 2px;
    color: var(--ink);
  }
  .brand-name--light { color: var(--white); }
  .identity {
    position: absolute; left: 60px; top: 150px; text-align: right; width: 200px;
  }
  .identity__name { font-weight: 700; font-size: 19px; color: var(--ink); letter-spacing: .3px; }
  .identity__title { font-size: 14px; color: var(--grey-text); margin-top: 4px; }
  .divider {
    position: absolute; left: 278px; top: 132px;
    width: 1px; height: 76px; background: var(--divider);
  }
  .contact { position: absolute; left: 296px; top: 132px; list-style: none; }
  .contact li {
    display: flex; align-items: center; gap: 8px;
    font-size: 14px; color: var(--grey-text); height: 25px;
  }
  .contact svg { width: 12px; height: 12px; fill: var(--ink); flex: none; }
  .address {
    position: absolute; left: 0; right: 0; top: 238px;
    text-align: center; font-size: 14px; color: var(--grey-text);
  }

  /* back */
  .truck-art {
    position: absolute; left: 0; top: 90px; width: 510px; height: 202px;
    background:
      radial-gradient(ellipse at 45% 60%, var(--art-tone) 0%, rgba(59,59,59,0.6) 45%, rgba(47,47,47,0) 75%),
      radial-gradient(ellipse at 70% 45%, var(--art-warm) 0%, rgba(47,47,47,0) 40%);
  }
  .brand-mark--back { left: 300px; top: 52px; }
</style>
</head>
<body>
  <section class="card card--front" aria-label="Business card front">
    <div class="brand-mark">
      <span class="brand-dot"></span>
      <span class="brand-name">VORLAN</span>
    </div>
    <div class="identity">
      <p class="identity__name">JONATHAN SMITH</p>
      <p class="identity__title">Manager</p>
    </div>
    <div class="divider"></div>
    <ul class="contact">
      <li><svg viewBox="0 0 24 24"><path d="M6.6 10.8a15 15 0 0 0 6.6 6.6l2.2-2.2a1 1 0 0 1 1-.25 11.4 11.4 0 0 0 3.6.57 1 1 0 0 1 1 1V20a1 1 0 0 1-1 1A17 17 0 0 1 3 4a1 1 0 0 1 1-1h3.5a1 1 0 0 1 1 1c0 1.25.2 2.45.57 3.6a1 1 0 0 1-.25 1z"/></svg>123-456-2100</li>
      <li><svg viewBox="0 0 24 24"><path d="M2 5h20v14H2z M2 5l10 8 10-8" /></svg>youremail@mailbox.com</li>
      <li><svg viewBox="0 0 24 24"><circle cx="12" cy="12" r="10"/></svg>www.yourwebsite.com</li>
    </ul>
    <p class="address">Your Address, City, State, Zip 0000</p>
  </section>

  <section class="card card--back" aria-label="Business card back">
    <div class="truck-art" role="img" aria-label="Large faint illustration of a flatbed tow truck"></div>
    <div class="brand-mark brand-mark--back">
      <span class="brand-dot"></span>
      <span class="brand-name brand-name--light">VORLAN</span>
    </div>
  </section>
</body>
</html>
```